Home page web design for a lawn specialist business

-The design must be based around the attached HPID (home page information design) called Turf Tidings HPID. I've attached Word and PDF versions - these are the same. The table boxes are just for approximate placement of information and you can use boxes and bold shapes for this design.

All fonts used in the HPID are only examples - you can use any Google font you wish.

- Text that is in orange is for your information only. Text to go on the design is black. Some instructions are in the HPID. Please be creative!

-The design needs to be modern and exciting - colours are to be the green of the logo, and white ...and then choose dark green, or dark grey or black.

Logo - attached (it's not great quality but don't worry, we'll replace it later)

- I've provided the images for the galleries - they are labelled and will match the name in the HPID. Please use the supplied images!

- Examples of some websites that have great design... don't copy them please but they are similar in look to what we are after....
www.qmbbuildworks.co.nz
http://www.rim-safeguard.co.nz/
http://www.lumenhomes.wb.gs/

Important: Width of content will be 1280 pixels when implemented as a web page but the winning design will need to supplied be on a 2000 pixel wide background so nav bars and background can extend outside the 1280 width.
Header height (without nav bar) 150-160 pixels.

We don't comment on individual designs but will choose a winning design promptly.

Industry/Entity Type

Business

Number of Pages Required

1 page

Font styles to use
Sans Serif

Requirements
Must have
• clean, modern, well-spaced design

```html
<!DOCTYPE html>
<html lang="en">
<head>
<meta charset="utf-8">
<title>Turf Tidings – Lawn specialists</title>
<link rel="stylesheet" href="https://fonts.googleapis.com/css2?family=Open+Sans:wght@400;600;700;800&display=swap">
<style>
:root{
  --page:#f4f6f2;
  --ink:#1e2a1f;
  --muted:#3d4a3e;
  --brand:#2f8a3a;
  --brand-dark:#1d5e2a;
  --grass-light:#cfe0b8;
  --grass-mid:#8fb46a;
  --photo-lawn:#3f8f3a;
  --photo-sky:#c9d3cf;
}
*{box-sizing:border-box;margin:0;padding:0}
html,body{width:1200px;height:561px;overflow:hidden}
body{background:var(--page);color:var(--ink);font-family:'Open Sans',Arial,sans-serif;position:relative}

.brand{position:absolute;left:40px;top:22px;display:flex;align-items:center;gap:14px}
.brand-mark{width:52px;height:52px;background:var(--brand);border-radius:4px}
.brand-name{font-size:28px;font-weight:800;color:var(--brand-dark);letter-spacing:-0.5px}

.header-info{position:absolute;right:40px;top:18px;text-align:right}
.header-title{font-size:19px;font-weight:700;color:var(--brand-dark)}
.header-tag{font-size:12px;margin-top:4px;color:var(--muted)}
.header-region{font-size:12px;color:var(--muted)}
.header-phone{font-size:20px;font-weight:800;margin-top:6px;letter-spacing:0.5px}

.main-nav{position:absolute;left:40px;right:40px;top:134px;height:36px;border-radius:3px;
  background:linear-gradient(180deg,var(--grass-light) 0%,var(--page) 45%,var(--grass-mid) 100%)}
.main-nav ul{list-style:none;display:flex;justify-content:space-between;align-items:center;height:100%;padding:0 26px}
.main-nav a{font-size:13.5px;font-weight:700;color:var(--ink);text-decoration:none}

.intro{position:absolute;left:28px;right:28px;top:186px}
.intro-title{text-align:center;font-size:18px;font-weight:700;color:var(--brand-dark)}
.intro-sub{text-align:center;font-size:12.5px;font-weight:600;margin-top:2px}
.intro p{font-size:11px;line-height:1.5;margin-top:9px;color:var(--muted)}

.service{position:absolute;text-align:center}
.service h2{font-size:24px;font-weight:700;color:var(--ink);letter-spacing:-0.3px}
.service-seeding{left:87px;top:340px;width:355px}
.service-care{left:703px;top:344px;width:402px}
.service-photo{display:block;margin-top:10px;border-radius:3px}
.service-seeding .service-photo{height:170px;background:linear-gradient(180deg,var(--photo-sky) 0%,var(--photo-lawn) 35%,var(--brand-dark) 100%)}
.service-care .service-photo{height:134px;margin-top:20px;background:linear-gradient(180deg,var(--photo-sky) 0%,#6f9a6a 30%,var(--photo-lawn) 60%,var(--brand) 100%)}
</style>
</head>
<body>
<header>
  <div class="brand"><span class="brand-mark"></span><span class="brand-name">Turf Tidings</span></div>
  <div class="header-info">
    <div class="header-title">Lawn specialists</div>
    <div class="header-tag">.....from ground preparation to lawn aftercare</div>
    <div class="header-region">Servicing the Auckland region</div>
    <div class="header-phone">0800 555 012</div>
  </div>
  <nav class="main-nav" aria-label="Main navigation">
    <ul>
      <li><a href="#">Home</a></li>
      <li><a href="#">About us</a></li>
      <li><a href="#">Services</a></li>
      <li><a href="#">Lawn care</a></li>
      <li><a href="#">Seasonal care</a></li>
      <li><a href="#">Hydroseeding</a></li>
      <li><a href="#">FAQs</a></li>
      <li><a href="#">Before &amp; After Gallery</a></li>
      <li><a href="#">Quote/Contact</a></li>
    </ul>
  </nav>
</header>
<main>
  <section class="intro">
    <h1 class="intro-title">You can always spot a Turf Tidings lawn</h1>
    <div class="intro-sub">It's The one that turns your neighbours green with envy.</div>
    <p>If you want a lawn or playing field that looks good throughout the year you talk to us. Turf Tidings are New Zealand's experts in high quality grass seeding and lawn maintenance, creating the lushest lawn you'll ever see. With high-tech equipment, years of experience and expert aftercare nobody knows grass like Turf Tidings.</p>
    <p>There are many factors that influence the quality of a lawn including seasonality, growing conditions, shade, seed types and time. A one-size-fits-all solution couldn't guarantee a great lawn, so we provide personalised advice and a full range of seeding techniques.</p>
  </section>
  <section class="service service-seeding">
    <h2>Grass seeding service</h2>
    <div class="service-photo" role="img" aria-label="Photo of freshly laid green lawn beside a paved path"></div>
  </section>
  <section class="service service-care">
    <h2>Lawn care maintenance</h2>
    <div class="service-photo" role="img" aria-label="Photo of a lawn mower cutting a green lawn with hedges behind"></div>
  </section>
</main>
</body>
</html>
```